Harbor Petroleum Business Cards

I would like to design some options for about 10 sets of double sided business cards for our team with a raised logo with a Silver glossy finished logo. We are a privately funded upstream Oil & Gas producer drilling vertical wells in Central Oklahoma with a long term production (ROI driven) strategy that we implement through an annual drilling program. We are focused on a shallow / vertical / long life / low decline strategy. We are based in downtown Tulsa Oklahoma. I have attached a sample business card and a picture of our hallway logo which we would like to replicate on the business cards.

Target Market(s)

SEC Accredited Investors and other Oil & Gas Operators

Industry/Entity Type

Upstream Oil & Gas

Contact Information for Business Card

You can see the sample photo attached, but email / website / address / direct phone / Cell Phone / Name / Title / Fax

Font styles to use
Other font styles liked:
• Felix Titling

Colors
0054AA
0677BA
7BADD7
CADEEF
E8F1F8

Requirements
Must have
• Glossy raised logo
Nice to have
• Possibly a new logo.
Should not have
• No Greens /

```html
<!DOCTYPE html>
<html lang="en">
<head>
<meta charset="utf-8">
<title>Harbor Petroleum Business Cards</title>
<link rel="stylesheet" href="https://fonts.googleapis.com/css2?family=Montserrat:wght@400;500&display=swap">
<style>
  :root {
    --backdrop: #2a2a2d;
    --card: #0b0b0c;
    --silver: #d9dcdf;
    --silver-soft: #b9bdc2;
    --rule: #8d9196;
  }
  * { margin: 0; padding: 0; box-sizing: border-box; }
  html, body { width: 1200px; height: 900px; overflow: hidden; }
  body {
    background: var(--backdrop);
    font-family: "Montserrat", sans-serif;
    color: var(--silver);
    position: relative;
  }
  .card {
    position: absolute;
    left: 250px;
    width: 700px;
    height: 400px;
    background: var(--card);
    border-radius: 22px;
  }
  .card-front { top: 40px; }
  .card-back { top: 460px; }

  .brand {
    display: flex;
    align-items: center;
    gap: 12px;
    font-weight: 500;
    color: var(--silver);
    text-transform: uppercase;
    letter-spacing: 0.08em;
    white-space: nowrap;
  }
  .brand-dot {
    border-radius: 50%;
    background: var(--silver);
    flex: none;
  }
  .card-front .brand {
    position: absolute;
    left: 50%; top: 50%;
    transform: translate(-50%, -50%);
    font-size: 30px;
  }
  .card-front .brand-dot { width: 20px; height: 20px; }

  .card-back .brand {
    position: absolute;
    left: 330px; top: 66px;
    transform: translateX(-50%);
    font-size: 18px;
  }
  .card-back .brand-dot { width: 13px; height: 13px; }

  .divider {
    position: absolute;
    left: 372px; top: 150px;
    width: 1px; height: 120px;
    background: var(--rule);
  }
  .holder {
    position: absolute;
    right: 348px; top: 208px;
    text-align: right;
  }
  .holder-name { font-size: 24px; font-weight: 400; letter-spacing: 0.02em; }
  .holder-title { font-size: 15px; color: var(--silver-soft); margin-top: 4px; }

  .contacts {
    position: absolute;
    left: 392px; top: 152px;
    list-style: none;
  }
  .contacts li {
    display: flex; align-items: center; gap: 12px;
    font-size: 14px; height: 23px;
  }
  .contacts svg { width: 13px; height: 13px; fill: var(--silver-soft); flex: none; }

  .address {
    position: absolute;
    left: 0; right: 0; top: 330px;
    text-align: center;
    padding-left: 180px;
    font-size: 15px;
  }
</style>
</head>
<body>
  <section class="card card-front" aria-label="Card front">
    <div class="brand"><span class="brand-dot"></span>Harbor Petroleum, LLC</div>
  </section>

  <section class="card card-back" aria-label="Card back">
    <div class="brand"><span class="brand-dot"></span>Harbor Petroleum, LLC</div>

    <div class="holder">
      <p class="holder-name">Dalen R. Whitacre, CPL</p>
      <p class="holder-title">Executive Vice President</p>
    </div>

    <div class="divider"></div>

    <ul class="contacts">
      <li>
        <svg viewBox="0 0 16 16"><path d="M2 6c0-2 2-3 6-3s6 1 6 3l-3 1-1-2H6L5 7 2 6zm2 2h8l1 6H3l1-6zm4 1.5a2 2 0 1 0 0 4 2 2 0 0 0 0-4z"/></svg>
        539-555-0142
      </li>
      <li>
        <svg viewBox="0 0 16 16"><path d="M4 1h8v14H4V1zm1.5 1.5v9h5v-9h-5zM8 12.3a.9.9 0 1 0 0 1.8.9.9 0 0 0 0-1.8z"/></svg>
        918-555-0187
      </li>
      <li>
        <svg viewBox="0 0 16 16"><path d="M4 1h7v4H4V1zM2 6h12v7h-2v2H4v-2H2V6zm3 5v3h6v-3H5z"/></svg>
        918-555-0163
      </li>
      <li>
        <svg viewBox="0 0 16 16"><path d="M1 3h14v10H1V3zm1.5 1.5L8 9l5.5-4.5v-.2h-11v.2z"/></svg>
        DRW@HPTulsa.com
      </li>
      <li>
        <svg viewBox="0 0 16 16"><path d="M8 1a7 7 0 1 0 0 14A7 7 0 0 0 8 1zm0 1.5c.9 0 1.8 1.8 2 4.5H6c.2-2.7 1.1-4.5 2-4.5zM2.6 7h2c.1-1.6.4-3 .9-3.9A5.5 5.5 0 0 0 2.6 7zm8.8 0h2a5.5 5.5 0 0 0-2.9-3.9c.5.9.8 2.3.9 3.9zM2.6 9a5.5 5.5 0 0 0 2.9 3.9c-.5-.9-.8-2.3-.9-3.9h-2zm3.4 0c.2 2.7 1.1 4.5 2 4.5s1.8-1.8 2-4.5H6zm5.4 0c-.1 1.6-.4 3-.9 3.9A5.5 5.5 0 0 0 13.4 9h-2z"/></svg>
        www.HarborPetroleumLLC.com
      </li>
    </ul>

    <p class="address">42 East 4th Street Suite 800 Tulsa, OK 74103</p>
  </section>
</body>
</html>
```